Van Wrap Design Painting Contractor Company

We need eye catching wrap design for painting contractor company
Has to be useable on our two van;; Velmont Carro production year 2001 ( white colour) , and Velmont Tisko Grando production year 2019 ( gray colour )
Sides and back of vans has to be similar

***Wrap design to include both sides, front hood and rear doors !!!!
***** since like our Company name is Brivo+ Norden wich mean that we act fast, the wrap design has to be in that way ( fast, trusted, strong)

I prefer red, green and blue colour, but I’m open for colour suggestions.
Has to be eye catching, memorable, noticeable and cool looking!!!!

Target Market(s)

Private and Commercial

Requirements
Must have
• 1. Logo, company name, phone number
2. Main Service description : SOBOSLIKAR
3. Secondary service description: Završni Radovi u Interijeru
4. website: BrivoNorden.net or just #BrivoNorden
Nice to have
• Icon:
1.Chatterleaf, Pixelgrove,
2.paintbrush, spray gunn on rear door
3. Company name on front bonnet
4. painter silhouette on ladder
Should not have
• ?

```html
<!DOCTYPE html>
<html lang="hr">
<head>
<meta charset="utf-8">
<title>Brivo Norden – Van Wrap</title>
<link href="https://fonts.googleapis.com/css2?family=Audiowide&family=Roboto:wght@400&display=swap" rel="stylesheet">
<style>
  :root {
    --wrap-red: #d91f26;
    --van-white: #f7f7f5;
    --van-line: #c9c9c9;
    --trim-dark: #3a3a3c;
    --glass: #5d6770;
    --tyre: #222224;
    --rim: #b8bcc0;
    --icon-peach: #f1c3ae;
    --canvas-bg: #ecedef;
    --text-white: #ffffff;
  }
  html, body { margin: 0; padding: 0; overflow: hidden; }
  body { width: 1100px; height: 1200px; background: var(--canvas-bg); }
  .van-side { display: block; width: 1100px; height: 598px; }
  .body-panel { fill: var(--van-white); stroke: var(--van-line); stroke-width: 2; }
  .wrap-field { fill: var(--wrap-red); }
  .window { fill: var(--glass); }
  .trim { fill: var(--trim-dark); }
  .tyre { fill: var(--tyre); }
  .rim { fill: var(--rim); }
  .url-pill { fill: var(--text-white); }
  .url-text { font-family: 'Audiowide', sans-serif; font-size: 19px; fill: var(--wrap-red); letter-spacing: 1.5px; }
  .brand-disc { fill: var(--text-white); }
  .brand-name { font-family: 'Audiowide', sans-serif; font-size: 38px; fill: var(--text-white); }
  .tagline { font-family: 'Roboto', sans-serif; font-size: 21px; fill: var(--text-white); }
  .service { font-family: 'Audiowide', sans-serif; font-size: 17px; fill: var(--text-white); letter-spacing: 0.5px; }
  .tick { fill: none; stroke: var(--text-white); stroke-width: 2; stroke-linecap: round; stroke-linejoin: round; }
  .social-name { font-family: 'Audiowide', sans-serif; font-size: 10px; fill: var(--text-white); }
  .tool-art { fill: var(--icon-peach); opacity: 0.75; }
</style>
</head>
<body>

<!-- Left side of the van -->
<svg class="van-side" viewBox="0 0 1100 598" xmlns="http://www.w3.org/2000/svg">
  <defs>
    <clipPath id="body-clip-left">
      <path d="M55 470 L55 395 Q62 345 110 320 L215 265 L300 120 Q310 112 330 112 L975 112 Q985 115 986 130 L990 470 Z"/>
    </clipPath>
  </defs>
  <path class="body-panel" d="M55 470 L55 395 Q62 345 110 320 L215 265 L300 120 Q310 112 330 112 L975 112 Q985 115 986 130 L990 470 Z"/>
  <g clip-path="url(#body-clip-left)">
    <circle class="wrap-field" cx="704" cy="293" r="218"/>
    <rect class="wrap-field" x="704" y="100" width="300" height="380"/>
  </g>
  <path class="window" d="M225 268 L290 155 Q298 142 315 141 L425 138 Q432 139 432 150 L432 272 Z"/>
  <rect class="trim" x="270" y="418" width="720" height="14"/>
  <rect class="trim" x="50" y="405" width="70" height="65" rx="10"/>
  <circle class="tyre" cx="194" cy="480" r="70"/><circle class="rim" cx="194" cy="480" r="42"/>
  <circle class="tyre" cx="817" cy="470" r="68"/><circle class="rim" cx="817" cy="470" r="41"/>

  <rect class="tool-art" x="235" y="308" width="172" height="99" rx="8" role="img" aria-label="Faint paint spray gun and paintbrush illustration"/>

  <rect class="url-pill" x="601" y="150" width="385" height="37" rx="18"/>
  <text class="url-text" x="790" y="176" text-anchor="middle">www.BrivoNorden.net</text>

  <circle class="brand-disc" cx="579" cy="268" r="62"/>
  <text class="brand-name" x="660" y="273">BrivoNorden</text>
  <text class="tagline" x="806" y="302" text-anchor="middle">Professional Services</text>

  <path class="tick" d="M639 346 l4 5 l9 -10"/>
  <text class="service" x="660" y="352">Završni Radovi u Interijeru</text>
  <path class="tick" d="M639 369 l4 5 l9 -10"/>
  <text class="service" x="660" y="375">SOBOSLIKAR</text>

  <text class="social-name" x="950" y="394" text-anchor="end">Talkwave · Pixelgrove</text>
</svg>

<!-- Right side of the van -->
<svg class="van-side" viewBox="0 0 1100 598" xmlns="http://www.w3.org/2000/svg">
  <defs>
    <clipPath id="body-clip-right">
      <path transform="translate(1100 0) scale(-1 1)" d="M55 470 L55 395 Q62 345 110 320 L215 265 L300 120 Q310 112 330 112 L975 112 Q985 115 986 130 L990 470 Z"/>
    </clipPath>
  </defs>
  <path class="body-panel" transform="translate(1100 0) scale(-1 1)" d="M55 470 L55 395 Q62 345 110 320 L215 265 L300 120 Q310 112 330 112 L975 112 Q985 115 986 130 L990 470 Z"/>
  <g clip-path="url(#body-clip-right)">
    <circle class="wrap-field" cx="396" cy="293" r="218"/>
    <rect class="wrap-field" x="96" y="100" width="300" height="380"/>
  </g>
  <g transform="translate(1100 0) scale(-1 1)">
    <path class="window" d="M225 268 L290 155 Q298 142 315 141 L425 138 Q432 139 432 150 L432 272 Z"/>
    <rect class="trim" x="270" y="418" width="720" height="14"/>
    <rect class="trim" x="50" y="405" width="70" height="65" rx="10"/>
    <circle class="tyre" cx="194" cy="480" r="70"/><circle class="rim" cx="194" cy="480" r="42"/>
    <circle class="tyre" cx="817" cy="470" r="68"/><circle class="rim" cx="817" cy="470" r="41"/>
  </g>

  <rect class="tool-art" x="693" y="308" width="169" height="99" rx="8" role="img" aria-label="Faint paintbrush and paint spray gun illustration"/>

  <rect class="url-pill" x="114" y="152" width="381" height="37" rx="18"/>
  <text class="url-text" x="320" y="178" text-anchor="middle">www.BrivoNorden.net</text>

  <circle class="brand-disc" cx="209" cy="266" r="62"/>
  <text class="brand-name" x="292" y="273">BrivoNorden</text>
  <text class="tagline" x="436" y="302" text-anchor="middle">Professional Services</text>

  <path class="tick" d="M221 347 l4 5 l9 -10"/>
  <text class="service" x="242" y="353">Završni Radovi u Interijeru</text>
  <path class="tick" d="M221 370 l4 5 l9 -10"/>
  <text class="service" x="242" y="376">SOBOSLIKAR</text>

  <text class="social-name" x="242" y="394">Talkwave · Pixelgrove</text>
</svg>

</body>
</html>
```